TORVIK - Handle Flow Solutions needs Friendbook Appearance

We have a website, www.torvik-example.eu / www.fittedLOOM-example.com. We are using social media until now on Chirplo, WorkNet, Quor and Vexa +. We would like to create a simple appearance of our company on Friendbook.

We have established TORVIK - Handled Flow Solutions and our Product Fitted LOOM in the last 4 years. The design of the site did not change since then and we would like to get a refresh.
The actual site is built on Word Press / Orlin and reachable under: www.torvik-example.eu / www.fittedLOOM-example.com / www.handledflowsolutions-example.com

The Logo and used colors should not change. We are in the industrial/regulated business and this should be reflected as well. We did that until now, without pictures of people because we are not a consulting company and we are not selling people.

We would like to see designs that transport our services on a world wide market (English/German). The final design should communicate sustainability, agility, lean and compliance (seriosity).

Target Market(s)

Agile is a new standard in the development paradigm and in the industry. The challenges of ‘Agile at Scale’ are realized every day. The only method out there for agility at scale is the Layered Nimble Method. TORVIK has direct access to the thought leadership and all the content of LOOM, the Layered Nimble Method, which is the de-facto standard for agility at scale. Combined with that we have access to Tiers, the world leading process management tool and we as system integrators have integrated both the framework and the platform into one product called Fitted LOOM.

Fitted LOOM works for those organizations who are in highly complex, highly compliant and auditable organizations such as Automotive, Defense, Aerospace, Medical and Finance. These organizations depend on their process and their process authoring and being able to stand up in terms of an audit or against an audit. TORVIK created the product Fitted LOOM which creates a dynamic where you can author your entire process and instantiate to your community internal or external and ensure that you have the best and most compliant process for your organization.

Industry/Entity Type

Media

Font styles to use
Sans Serif

Requirements
Must have
• Transform our image and messages from blog in Wordpress on torvik-example.eu/blog
Nice to have
• Additional functioanaliy
Should not have
• no childern, faces of persones etc.

```html
<!DOCTYPE html>
<html lang="en">
<head>
<meta charset="utf-8">
<title>TORVIK – Friendbook Page</title>
<link href="https://fonts.googleapis.com/css2?family=Montserrat:wght@300;700&family=Arimo:wght@400;700&display=swap" rel="stylesheet">
<style>
  :root {
    --page-bg: #ffffff;
    --bar-blue: #3b5998;
    --bar-line: #2d4373;
    --canvas-grey: #e9ebee;
    --card-white: #ffffff;
    --card-border: #dddfe2;
    --text-dark: #1d2129;
    --text-muted: #4b4f56;
    --nav-active: #dadde1;
    --brand-navy: #1f2f4f;
    --brand-grey: #6b7380;
    --cta-blue: #4080ff;
    --cover-deep: #07163f;
    --cover-mid: #1c4ea3;
    --cover-light: #8fb3e6;
  }
  * { box-sizing: border-box; margin: 0; padding: 0; }
  html, body { width: 1200px; height: 768px; overflow: hidden; background: var(--page-bg); }
  body { position: relative; font-family: "Arimo", Helvetica, Arial, sans-serif; }

  .page-frame { position: absolute; left: 60px; top: 211px; width: 1080px; height: 346px; background: var(--canvas-grey); }

  .top-bar { position: absolute; left: 0; top: 0; width: 1080px; height: 34px; background: var(--bar-blue); border-bottom: 1px solid var(--bar-line); }
  .site-name { position: absolute; left: 60px; top: 10px; width: 80px; text-align: right; color: #fff; font-size: 11px; font-weight: 700; white-space: nowrap; }
  .search-field { position: absolute; left: 146px; top: 6px; width: 355px; height: 19px; background: #fff; border-radius: 2px; font-size: 11.5px; color: var(--text-dark); line-height: 19px; padding-left: 8px; }
  .search-button { position: absolute; right: 0; top: 0; width: 38px; height: 19px; background: #f6f7f9; border-left: 1px solid var(--card-border); }
  .search-button svg { position: absolute; left: 13px; top: 4px; }
  .user-chip { position: absolute; left: 659px; top: 6px; display: flex; align-items: center; gap: 6px; color: #fff; font-size: 10px; font-weight: 700; }
  .user-avatar { width: 18px; height: 18px; background: linear-gradient(135deg, #8a6e5e, #3a2c26); border-radius: 1px; }
  .bar-link { position: absolute; left: 749px; top: 12px; color: #fff; font-size: 10px; font-weight: 700; padding-left: 8px; border-left: 1px solid var(--bar-line); }
  .bar-icons { position: absolute; left: 800px; top: 8px; display: flex; gap: 11px; }
  .settings-icon { position: absolute; left: 899px; top: 11px; }

  .profile-card { position: absolute; left: 120px; top: 44px; width: 134px; height: 135px; background: var(--card-white); border: 1px solid var(--card-border); border-radius: 2px; padding: 3px; }
  .profile-inner { width: 100%; height: 100%; border: 1px solid #ccd0d5; display: flex; flex-direction: column; align-items: center; justify-content: center; }
  .profile-name { font-family: "Montserrat", sans-serif; font-weight: 700; font-size: 22px; color: var(--brand-navy); letter-spacing: 0.5px; border-bottom: 1px solid var(--brand-navy); line-height: 1; padding-bottom: 1px; }
  .profile-tagline { font-size: 8.5px; color: var(--brand-grey); margin-top: 3px; }

  .side-nav { position: absolute; left: 118px; top: 203px; width: 140px; list-style: none; font-size: 11.5px; color: var(--text-muted); }
  .side-nav li { height: 25.6px; line-height: 25.6px; padding-left: 8px; }
  .side-nav .is-active { background: var(--nav-active); border-left: 2px solid var(--bar-blue); color: var(--text-dark); }

  .cover { position: absolute; left: 265px; top: 35px; width: 665px; height: 252px; overflow: hidden;
    background: linear-gradient(100deg, var(--cover-deep) 0%, #0c2560 38%, var(--cover-mid) 62%, var(--cover-light) 82%, #3b6cc0 100%); }
  .cover-photo { position: absolute; inset: 0; }
  .cover-copy { position: absolute; left: 38px; top: 28px; color: #fff; font-family: "Montserrat", sans-serif; }
  .cover-brand { font-weight: 700; font-size: 34px; letter-spacing: 1px; line-height: 1; margin-bottom: 10px; }
  .cover-headline { font-weight: 700; font-size: 21px; line-height: 26px; letter-spacing: -0.3px; text-transform: uppercase; }
  .cover-sub { font-weight: 300; font-size: 21px; line-height: 26px; }

  .action-row { position: absolute; left: 265px; top: 287px; width: 664px; height: 40px; background: var(--card-white); border: 1px solid var(--card-border); border-top: 0; }
  .action-group { position: absolute; left: 11px; top: 9px; display: flex; border: 1px solid #ccd0d5; border-radius: 2px; background: #f6f7f9; height: 22px; }
  .action-button { display: flex; align-items: center; gap: 4px; padding: 0 9px; font-size: 10px; font-weight: 700; color: var(--text-muted); border-right: 1px solid #ccd0d5; }
  .action-button:last-child { border-right: 0; }
  .contact-button { position: absolute; left: 414px; top: 8px; width: 239px; height: 22px; background: var(--cta-blue); color: #fff; font-size: 11.5px; text-align: center; line-height: 22px; border-radius: 2px; }
</style>
</head>
<body>
  <div class="page-frame">
    <header class="top-bar">
      <span class="site-name">Friendbook</span>
      <div class="search-field">mockupyard-example.com
        <span class="search-button"><svg width="11" height="11" viewBox="0 0 11 11"><circle cx="4.5" cy="4.5" r="3.5" fill="none" stroke="#4b4f56" stroke-width="1.3"/><line x1="7" y1="7" x2="10" y2="10" stroke="#4b4f56" stroke-width="1.3"/></svg></span>
      </div>
      <div class="user-chip"><span class="user-avatar" role="img" aria-label="User profile photo"></span>Alex Marlow</div>
      <span class="bar-link">Home</span>
      <div class="bar-icons">
        <svg width="18" height="16" viewBox="0 0 18 16" aria-label="Friend requests"><circle cx="7" cy="4" r="3" fill="#fff"/><path d="M1 15c0-5 12-5 12 0z" fill="#fff"/><circle cx="12.5" cy="5" r="2.5" fill="#fff"/><path d="M11 9c3 0 6 1 6 5h-3z" fill="#fff"/></svg>
        <svg width="18" height="16" viewBox="0 0 18 16" aria-label="Messages"><path d="M4 2h13v9h-3l-2 2v-2H4z" fill="#fff"/><path d="M1 5h2v7h7v2H5l-2 2v-2H1z" fill="#fff"/></svg>
        <svg width="16" height="16" viewBox="0 0 16 16" aria-label="Notifications"><circle cx="8" cy="8" r="7.5" fill="#fff"/><path d="M4 4c2 0 3 2 2 4s1 3 0 5M10 3c0 2 2 2 3 4" stroke="#3b5998" stroke-width="1.6" fill="none"/></svg>
      </div>
      <svg class="settings-icon" width="30" height="10" viewBox="0 0 30 10" aria-label="Settings"><rect x="0" y="3" width="7" height="6" fill="#fff"/><rect x="2" y="0" width="3" height="4" fill="#fff"/><rect x="8" y="2" width="5" height="1.4" fill="#fff"/><rect x="8" y="5" width="5" height="1.4" fill="#fff"/><rect x="8" y="8" width="5" height="1.4" fill="#fff"/><path d="M20 3h8l-4 5z" fill="#fff"/></svg>
    </header>

    <div class="profile-card">
      <div class="profile-inner">
        <span class="profile-name">TORVIK</span>
        <span class="profile-tagline">Handled Flow Solutions</span>
      </div>
    </div>

    <ul class="side-nav">
      <li class="is-active">Home</li>
      <li>Photos</li>
      <li>Likes</li>
    </ul>

    <section class="cover">
      <div class="cover-photo" role="img" aria-label="Blue-toned close-up of a milling cutter above a machined engine block"></div>
      <div class="cover-copy">
        <div class="cover-brand">TORVIK</div>
        <div class="cover-headline">- Handled Flow<br>Solutions Compliance</div>
        <div class="cover-sub">&amp; efficiency for your<br>software development</div>
      </div>
    </section>

    <div class="action-row">
      <div class="action-group">
        <span class="action-button"><svg width="10" height="10" viewBox="0 0 10 10"><rect x="0" y="4" width="2" height="6" fill="#4267b2"/><path d="M3 4l3-4c1 0 1 1 1 2l-1 2h4v2l-2 4H3z" fill="#4267b2"/></svg>Liked <svg width="7" height="4"><path d="M0 0h7L3.5 4z" fill="#4b4f56"/></svg></span>
        <span class="action-button"><svg width="10" height="10" viewBox="0 0 10 10"><circle cx="5" cy="5" r="5" fill="#bec3c9"/></svg>Message</span>
        <span class="action-button"><svg width="12" height="3"><circle cx="1.5" cy="1.5" r="1.2" fill="#90949c"/><circle cx="6" cy="1.5" r="1.2" fill="#90949c"/><circle cx="10.5" cy="1.5" r="1.2" fill="#90949c"/></svg>More <svg width="7" height="4"><path d="M0 0h7L3.5 4z" fill="#4b4f56"/></svg></span>
      </div>
      <span class="contact-button">Contact Us</span>
    </div>
  </div>
</body>
</html>
```